Zielgruppe
Wir installieren Kälteanlagen für die Industrie, das Gewerbe und Privat. Kälteanlagen mit natürlichem Kältemittel CO2 und Klimaanlagen.
Aufgabenstellung
In unserem Eingangsbereich befindet sich ein Raumtrenner (siehe beigefügte Bilder). Darauf steht ein restaurierter historischer Kältekompressor. Ein altes Prospekt dieser Maschine finden Sie im Anhang. Wir würden gerne hinten auf dem Ständer eine beklebte Glasscheibe anbringen um unsere Besucher zu begrüßen und ggf. ein paar Infos zu dem Kältekompressor zu geben. Dafür soll ein Design erstellt werden. Die Fläche hinter dem Kompressor ist ca. 1,60 x 1,60 m groß. Der Kältekompressor an seinem höchsten Punkt ca. 1,10 m. Die Glasscheibe würden wir ca. 1,40 m x 0,8 m hoch machen, die wäre also teilweise verdeckt von dem Kompressor.

```html
<!DOCTYPE html>
<html lang="de">
<head>
<meta charset="utf-8">
<title>Willkommen – Unser Kältekompressor</title>
<link href="https://fonts.googleapis.com/css2?family=Caveat:wght@400&family=Raleway:wght@300;400;600&display=swap" rel="stylesheet">
<style>
  :root {
    --brand-blue: #4a80b8;
    --ink: #111111;
    --paper: #ffffff;
  }
  html, body {
    margin: 0;
    padding: 0;
    overflow: hidden;
    background: var(--paper);
  }
  .canvas {
    position: relative;
    width: 1200px;
    height: 681px;
    overflow: hidden;
    background: var(--paper);
    font-family: "Raleway", sans-serif;
    color: var(--ink);
  }
  .greeting {
    position: absolute;
    left: 72px;
    top: 8px;
    margin: 0;
    font-family: "Caveat", cursive;
    font-weight: 400;
    font-size: 104px;
    line-height: 1;
    color: var(--brand-blue);
  }
  .header-band {
    position: absolute;
    left: 497px;
    top: 79px;
    width: 488px;
    height: 25px;
    background: var(--brand-blue);
  }
  .header-band--tail {
    left: 985px;
    top: 101px;
    width: 215px;
    height: 12px;
  }
  .brand-square {
    position: absolute;
    left: 986px;
    top: 38px;
    width: 64px;
    height: 64px;
    background: var(--brand-blue);
  }
  .brand-name {
    position: absolute;
    right: 228px;
    top: 46px;
    margin: 0;
    font-family: "Raleway", sans-serif;
    font-weight: 600;
    font-size: 17px;
    color: var(--brand-blue);
    white-space: nowrap;
  }
  .title {
    position: absolute;
    left: 0;
    width: 1234px;
    top: 182px;
    margin: 0;
    text-align: center;
    font-weight: 600;
    font-size: 64px;
    line-height: 1;
  }
  .subtitle {
    position: absolute;
    left: 0;
    width: 1260px;
    top: 268px;
    margin: 0;
    text-align: center;
    font-weight: 300;
    font-size: 64px;
    line-height: 1;
    color: var(--brand-blue);
  }
  .facts {
    position: absolute;
    left: 79px;
    top: 398px;
    width: 1080px;
    margin: 0;
    padding: 0;
    list-style: none;
    font-weight: 400;
    font-size: 28.5px;
    line-height: 29px;
  }
  .facts li { margin: 0 0 23px 0; }
  .highlight { color: var(--brand-blue); }
</style>
</head>
<body>
  <main class="canvas">
    <h2 class="greeting">Willkommen</h2>

    <div class="header-band"></div>
    <div class="header-band header-band--tail"></div>
    <p class="brand-name">Kessler Elektro-Kältebau</p>
    <div class="brand-square"></div>

    <h1 class="title">Unser Kältekompressor</h1>
    <p class="subtitle">Wusstest du?</p>

    <ul class="facts">
      <li>… dass der Kältekompressor trotz hoher Leistung <span class="highlight">wenig Platzbedarf</span> hat.</li>
      <li>… dass der Hochleistungs-Bündelrohrverflüssiger, der im Grundgestell eingebaut wurde leicht zugänglich ist und man ihn daher <span class="highlight">besser reinigen</span> kann.</li>
      <li>… dass der Kältekompressor einen <span class="highlight">niedrigen Stromverbauch</span> hat.</li>
      <li>… dass sich der Kältekompressor <span class="highlight">selbstständig regeln</span> kann.</li>
    </ul>
  </main>
</body>
</html>
```